Building company with a modern and unique product looking for a business card to help us stand out

We currently have a logo but as our business has grown, we feel that our business card is not reflecting our modern and high quality product and help us stand out from the crowd. Our business is mainly in the construction of new homes using a unique method and materials that makes our homes fire proof, vermin and pest resistant and rated to the maximum cyclone category (category 5). We need a business card that helps us stand out as well as communicating professionalism, high quality and trustworthiness. I have attached our current logo with a black and white option, as well as our business card which is double sided. We would like to retain as much of the information that is currently on our business cards, but presented in a more sleek way. We do like our current colour palette ( white, black, yellow and grey) and have been looking primarily at business cards with a black background however we are open to other combinations of colour and layout as long as we stand out. Please feel free to tweak our logo to make it more suitable for a business card, we like the black option that we use but we have had trouble trying to get the white area to match the rest of the logo and blend effectively into a business card. Please do not hesitate to contact us with any questions as we really want this to be successful!

Target Market(s)

Large contracts including government and larger companies

Industry/Entity Type

Business

We will be providing this business card to potential clients including key government ministers and large funding companies, our business card should show that we are professional and reliable.

Requirements
Must have
• It must be easy to read and pleasing to the eye, It must contain as much of the information on the current business card and unless something really stands out, we will most likely pick a design that has all of the information included. It must include our logo of course and have some colour included.
Nice to have
• We are looking for a high end business card and would like to see designs that reflect this. We like the gloss/matte contrast, plastic cards with opaque/coloured areas and unique features not seen on everyday paper business cards. It would be nice to see a few different colour combinations, we are open to new ideas so please feel free to take some artistic licence.
Should not have
• Must not be too busy, difficult to read or be distracting from the information conveyed. Other than this please feel free to add your own touches and make it unique!

```html
<!DOCTYPE html>
<html lang="en">
<head>
<meta charset="utf-8">
<title>Ridgeline Building Co. — Business Card</title>
<link href="https://fonts.googleapis.com/css2?family=Great+Vibes&family=Josefin+Sans:wght@400;600&display=swap" rel="stylesheet">
<style>
  :root {
    --card-white: #ffffff;
    --panel-black: #000000;
    --edge-grey: #6b6b6b;
    --accent-gold: #f0d46a;
    --ink-black: #111111;
  }
  html, body {
    margin: 0;
    padding: 0;
    overflow: hidden;
    background: var(--card-white);
  }
  .card {
    position: relative;
    width: 1200px;
    height: 679px;
    overflow: hidden;
    background: var(--card-white);
  }
  .card__panel {
    position: absolute;
    inset: 0;
    width: 1200px;
    height: 679px;
  }
  .card__name {
    position: absolute;
    left: 22px;
    top: 100px;
    margin: 0;
    font-family: "Great Vibes", cursive;
    font-weight: 400;
    font-size: 96px;
    line-height: 1;
    color: var(--accent-gold);
    white-space: nowrap;
  }
  .card__role {
    position: absolute;
    left: 26px;
    top: 226px;
    margin: 0;
    font-family: "Josefin Sans", sans-serif;
    font-weight: 400;
    font-size: 46px;
    line-height: 1;
    color: var(--accent-gold);
  }
  .card__contacts {
    position: absolute;
    left: 30px;
    top: 440px;
    margin: 0;
    padding: 0;
    list-style: none;
    font-family: "Josefin Sans", sans-serif;
    font-weight: 400;
    font-size: 34px;
    line-height: 1;
    color: var(--accent-gold);
  }
  .card__contacts li { margin-bottom: 22px; white-space: nowrap; }
  .card__contacts li:last-child { margin-top: 8px; }
  .brand {
    position: absolute;
    left: 790px;
    top: 130px;
    width: 340px;
    display: flex;
    flex-direction: column;
    align-items: center;
    gap: 22px;
  }
  .brand__mark {
    width: 56px;
    height: 56px;
    background: var(--accent-gold);
  }
  .brand__name {
    margin: 0;
    font-family: "Josefin Sans", sans-serif;
    font-weight: 600;
    font-size: 40px;
    line-height: 1.15;
    text-align: center;
    color: var(--ink-black);
  }
</style>
</head>
<body>
  <main class="card">
    <svg class="card__panel" viewBox="0 0 1200 679" aria-hidden="true">
      <polygon points="0,0 560,0 790,400 655,679 0,679" fill="var(--edge-grey)"/>
      <polygon points="0,0 546,0 775,400 641,679 0,679" fill="var(--panel-black)"/>
    </svg>

    <h1 class="card__name">Callum Reyes</h1>
    <p class="card__role">Managing Director</p>

    <ul class="card__contacts">
      <li>mobile: (02) 55 310 486</li>
      <li>phone: 0491 570 213</li>
      <li>email: ridgelinebuild@example.com</li>
    </ul>

    <div class="brand">
      <div class="brand__mark"></div>
      <p class="brand__name">Ridgeline<br>Building Co.</p>
    </div>
  </main>
</body>
</html>
```